Looking for potential sellers

We help people buy and sell homes and are currently looking for potential home sellers. We offer low commissions, are the Local Colorado Springs and Falcon Experts, homes selling fast and at top dollar, Free expert pricing opinions and Consultations, over 9 years of experience, top rated Realtors creative and aggressive marketing strategies. Never merely own a house, THRIVE at Harborview. phone number 482-630-9157 web thriveatharborview.com

```html
<!DOCTYPE html>
<html lang="en">
<head>
<meta charset="utf-8">
<title>Keystone Harbor Realty Postcard</title>
<link rel="stylesheet" href="https://fonts.googleapis.com/css2?family=Montserrat:wght@700&family=Quicksand:wght@400;500;700&display=swap">
<style>
  :root {
    --frame: #2f2f2f;
    --paper: #ffffff;
    --olive: #b3b36a;
    --ink: #2b2b22;
    --rule: #555555;
    --map-land: #e4dfd7;
    --map-green: #c3dda1;
  }
  * { box-sizing: border-box; margin: 0; padding: 0; }
  html, body { width: 1200px; height: 814px; overflow: hidden; background: var(--frame); }
  .postcard {
    position: absolute; left: 7px; top: 8px; width: 1182px; height: 796px;
    background: var(--paper); overflow: hidden;
  }
  .front-panel {
    position: absolute; left: 0; top: 0; width: 622px; height: 796px; background: var(--olive);
  }
  .headline {
    position: absolute; left: 35px; top: 56px;
    font-family: "Montserrat", sans-serif; font-weight: 700;
    font-size: 37px; line-height: 46px; color: var(--ink); letter-spacing: -0.3px;
  }
  .intro {
    position: absolute; left: 35px; top: 168px; width: 575px;
    font-family: "Quicksand", sans-serif; font-weight: 400;
    font-size: 21px; line-height: 32.2px; color: var(--ink);
  }
  .map-area {
    position: absolute; left: 0; top: 464px; width: 622px; height: 314px;
    background: linear-gradient(90deg, var(--map-green) 0%, #d3dcb9 18%, var(--map-land) 32%, var(--map-land) 100%);
  }
  .footer-strip { position: absolute; left: 0; top: 778px; width: 622px; height: 18px; background: var(--olive); }
  .mail-address {
    position: absolute; left: 661px; top: 47px; font-style: normal;
    font-family: "Quicksand", sans-serif; font-weight: 500; font-size: 14.5px; line-height: 20.5px; color: #111;
  }
  .mail-address strong { font-weight: 700; }
  .postage-box {
    position: absolute; left: 1075px; top: 33px; width: 81px; height: 81px;
    border: 1.5px solid #444; display: flex; align-items: center; justify-content: center;
    font-family: "Quicksand", sans-serif; font-weight: 500; font-size: 12.5px; color: #111;
  }
  .address-line { position: absolute; left: 661px; width: 495px; height: 2px; background: var(--rule); }
  .seller-pitch {
    position: absolute; left: 661px; top: 560px; width: 495px;
    font-family: "Quicksand", sans-serif; color: #111;
  }
  .seller-pitch h2 { font-family: "Montserrat", sans-serif; font-weight: 700; font-size: 17px; margin-bottom: 8px; color: var(--ink); }
  .seller-pitch ul { list-style: none; font-size: 13.5px; line-height: 20px; font-weight: 500; }
  .seller-pitch li::before { content: "✓ "; color: #7f7f3c; font-weight: 700; }
  .seller-contact { margin-top: 10px; font-size: 14.5px; font-weight: 700; }
</style>
</head>
<body>
  <div class="postcard">
    <section class="front-panel">
      <h1 class="headline">Never Merely Own a House.<br>THRIVE at Harborview.</h1>
      <p class="intro">Keystone Harbor Realty, and our lead broker Dale<br>Porter, have been helping clients find their dream<br>home in beautiful Colorado Springs and its surround-<br>ing areas since 2009. We know that buying or selling<br>your home can be one of the most exciting (and<br>sometimes trying) times of your life. Because of this,<br>we make a concerted effort to know and understand<br>your wants and needs, which plays a crucial part in<br>both your success, and ours.</p>
      <div class="map-area" role="img" aria-label="Map of northern Colorado Springs showing current home listings"></div>
      <div class="footer-strip"></div>
    </section>

    <address class="mail-address">
      <strong>Keystone Harbor Realty</strong><br>
      1840 Mariner Building<br>
      615 Wexford Avenue<br>
      Colorado Springs, CO 80917
    </address>
    <div class="postage-box">POSTAGE</div>
    <div class="address-line" style="top:276px"></div>
    <div class="address-line" style="top:341px"></div>
    <div class="address-line" style="top:400px"></div>
    <div class="address-line" style="top:465px"></div>

    <section class="seller-pitch">
      <h2>Thinking of selling your home?</h2>
      <ul>
        <li>Low commissions, homes selling fast and at top dollar</li>
        <li>Free expert pricing opinions and consultations</li>
        <li>Local Colorado Springs and Falcon experts, 9+ years</li>
      </ul>
      <p class="seller-contact">482-630-9157 &nbsp;·&nbsp; thriveatharborview.com</p>
    </section>
  </div>
</body>
</html>
```